business card double side design

We need a business card design for our company PLUMlearnhub. DOUBLE SIDED. We provide continuing education programs & courses across North America. Our website is www.plumlearnhub.example - please use the grey pinstrip concept as part of the design. Compliment the branding that is occuring on that site!
Please use pantones daa520 and 3f3151. Verdana for text. I have attached our logo.
I would like the logo & website address www.PLUMlearnhub.example on the front of the card, all other info on the backside. The final design should communicate authority and credibility.

• verdanda

• pantones daa520 and 3f3151. Verdana for text.
• must compliment the branding occuring on the www.PLUMlearnhub.example

```html
<!DOCTYPE html>
<html lang="en">
<head>
<meta charset="utf-8">
<title>PLUMlearnhub – Business Card, Front and Back</title>
<link rel="stylesheet" href="https://fonts.googleapis.com/css2?family=Noto+Sans:wght@400;700&display=swap">
<style>
  :root {
    --gold: #daa520;
    --plum: #3f3151;
    --paper: #f4f4f4;
    --paper-shade: #dcdcdc;
    --text-light: #f2f0f5;
    --stage: #6fcfbc;
  }
  * { box-sizing: border-box; margin: 0; padding: 0; }
  html, body {
    width: 1200px;
    height: 640px;
    overflow: hidden;
  }
  body {
    background: var(--stage);
    font-family: Verdana, "Noto Sans", sans-serif;
    position: relative;
  }

  .card {
    position: absolute;
    top: 180px;
    width: 490px;
    height: 280px;
    border-radius: 44px 0 44px 0;
    overflow: hidden;
    box-shadow: 0 18px 30px rgba(0, 0, 0, 0.18);
  }

  /* ---------- Front ---------- */
  .card-front {
    left: 80px;
    background: var(--paper);
  }
  .front-texture {
    position: absolute;
    inset: 0;
    background:
      linear-gradient(135deg, rgba(255,255,255,0.9) 0%, rgba(230,230,230,0.6) 35%, rgba(255,255,255,0.85) 60%, rgba(215,215,215,0.5) 100%),
      var(--paper-shade);
  }
  .brand-lockup {
    position: absolute;
    left: 44px;
    top: 92px;
    display: flex;
    align-items: center;
    gap: 18px;
  }
  .brand-dot {
    width: 64px;
    height: 64px;
    border-radius: 50%;
    background: var(--gold);
  }
  .brand-name {
    font-size: 36px;
    font-weight: 700;
    color: var(--plum);
    letter-spacing: -0.5px;
  }
  .front-band {
    position: absolute;
    left: 0;
    right: 0;
    bottom: 0;
    height: 52px;
    background: var(--plum);
    border-top: 6px solid var(--gold);
    display: flex;
    align-items: center;
    justify-content: flex-end;
    padding-right: 44px;
  }
  .front-url {
    font-size: 13px;
    color: var(--text-light);
    letter-spacing: 0.3px;
  }

  /* ---------- Back ---------- */
  .card-back {
    left: 630px;
    background: var(--plum);
    color: var(--text-light);
    padding: 34px 40px;
  }
  .slogan {
    font-size: 15px;
    line-height: 1.2;
  }
  .tagline {
    font-size: 9.5px;
    color: var(--gold);
    margin-top: 2px;
  }
  .contact-list {
    list-style: none;
    margin-top: 22px;
    font-size: 13.5px;
    line-height: 1.45;
  }
  .contact-list li {
    display: flex;
    align-items: center;
    gap: 8px;
    padding-left: 24px;
  }
  .contact-list li.has-icon { padding-left: 0; }
  .contact-icon {
    width: 16px;
    height: 16px;
    flex: none;
  }
</style>
</head>
<body>

  <section class="card card-front" aria-label="Business card front">
    <div class="front-texture" role="img" aria-label="Soft grey faceted pinstripe background texture"></div>
    <div class="brand-lockup">
      <span class="brand-dot" aria-hidden="true"></span>
      <span class="brand-name">PLUMlearnhub</span>
    </div>
    <div class="front-band">
      <span class="front-url">www.PLUMlearnhub.example</span>
    </div>
  </section>

  <section class="card card-back" aria-label="Business card back">
    <p class="slogan">Advance Your Expertise Now</p>
    <p class="tagline">Lifelong Learning Across North America</p>
    <ul class="contact-list">
      <li>Technical:&nbsp; Dana Whitfield</li>
      <li class="has-icon">
        <svg class="contact-icon" viewBox="0 0 16 16" aria-hidden="true">
          <circle cx="8" cy="8" r="8" fill="var(--gold)"/>
          <rect x="4" y="5" width="8" height="6" rx="1" fill="none" stroke="var(--plum)" stroke-width="1.2"/>
          <path d="M4 5.5 L8 8.5 L12 5.5" fill="none" stroke="var(--plum)" stroke-width="1.2"/>
        </svg>
        dana@PLUMlearnhub.example
      </li>
      <li class="has-icon">
        <svg class="contact-icon" viewBox="0 0 16 16" aria-hidden="true">
          <circle cx="8" cy="8" r="8" fill="var(--gold)"/>
          <path d="M5.5 4 L7 4 L7.6 6.2 L6.7 7 Q7.6 8.8 9 9.3 L9.8 8.4 L12 9 L12 10.5 Q12 11.6 10.8 11.6 Q5 11 4.4 5.2 Q4.4 4 5.5 4 Z" fill="var(--plum)"/>
        </svg>
        555.014.2290
      </li>
      <li>support@PLUMlearnhub.example</li>
    </ul>
  </section>

</body>
</html>
```